NOTE: I PROVIDED THE INCORRECT LOGO AND ONLY A HANDFUL OF PEOPLE NOTICED THAT IT WAS NOT THE ONE I DESCRIBED. THE LOGO I HAVE NOW ATTACHED MATCHES MY WEBSITE AND THE COLORS ON THE WEBSITE SHOULD BE USED FOR THE CARD.

PLEASE READ THE BUSINESS CARD DETAILS AND PROJECT MUST HAVES CAREFULLY.

I am looking for a business card that is powerful, a bit edgy, and although I work in the corporate world, not too formal. I would like to see designs that use the colors on my website www.brightmoorlane.com. I don't want the card to look washed out so please use shades of those colors that make them "pop". The "vibe" of the card needs to show substance and confidence while also reflecting that we're not your usual consultants.

The focus of my work is turning "people problems" into profits. Those problems could be poor service, an unstable workforce, untrained leaders, or managing change. We are an aggressive, results-focused team of performance improvement professionals who refuse to believe "things can't be done". For us, failure is not an option. Our logo reflects a target from the view of the site on a gun.

In addition to the contact information provided on the sample business card (do not include "turning people problems into profits"), I would like to include this statement (probably on the back):
I equip results-oriented business leaders to turn their people problems into profits in six months or less.

PLEASE NOTE THAT MY WEBSITE IS UNDER REVISION TO TONE DOWN THE MILITARY THEME, ALTHOUGH THE WARRIOR ENERGY AND FOCUS ON RESULTS REMAINS.

Target Market(s)

My clients are Mid and senior-level managers. I don't target any particular industry.

Industry/Entity Type

Consulting

Contact Information for Business Card

In addition to the contact information provided on the sample business card (DO NOT INCLUDE "turning people problems into profits"), I would like to include this statement (probably on the back):

I don't care whether the card is landscape or portrait view.

Font styles to use
Sans Serif

Requirements
Must have
• 1. be easy to read, no 6-8 point fonts!
• 2. a "vibe" that captures the eye without being too chaotic or busy
• 3. bold color, not washed out or boring - a good blend with the colors currently on my website (black, red, white, army green) but you don't need to use all of them.
• 4. all the contact information I have provided
• 5. a good blend with the colors currently on my website
• 6. Must have this quote on the back of the card: I equip results-oriented business leaders to turn their people problems into profits in six months or less.
Nice to have
• In looking at the sample images I provided for ideas, you can see that I like the way a card carries over from one side to the next.
• It would be great to find some aspect/quality/feature that I haven't seen before
Should not have
• 1. NO use of ALL CAPS
• 2. fonts that I would have to seek out and purchase (you should provide files for font if using something not standard)

```html
<!DOCTYPE html>
<html lang="en">
<head>
<meta charset="utf-8">
<title>Brightmoor Lane Inc — Business Card</title>
<link href="https://fonts.googleapis.com/css2?family=Roboto+Condensed:wght@400;700&family=Graduate&family=Montserrat:wght@400&display=swap" rel="stylesheet">
<style>
  :root {
    --stage: #e9eaec;
    --card-white: #ffffff;
    --card-black: #222222;
    --lime: #a6ce39;
    --lime-text: #9ccc2f;
    --navy-blue: #3a6d93;
    --sky-blue: #4fb4e8;
    --forest: #2f5f45;
    --ink: #1f1f1f;
    --label-blue: #2f6a9c;
    --rule-green: #3c6e52;
    --muted: #444444;
  }
  * { box-sizing: border-box; margin: 0; padding: 0; }
  html, body { width: 1200px; height: 900px; overflow: hidden; }
  body {
    background: var(--stage);
    font-family: "Roboto Condensed", "Arial Narrow", sans-serif;
    position: relative;
  }
  .card {
    position: absolute;
    width: 680px;
    height: 389px;
    left: 260px;
    border-radius: 4px;
    overflow: hidden;
    box-shadow: 0 6px 18px rgba(0,0,0,0.18);
  }

  /* Back side */
  .card-back { top: 40px; background: var(--card-black); }
  .mission {
    position: absolute;
    left: 44px; top: 58px;
    width: 400px;
    font-family: "Graduate", serif;
    font-size: 27px;
    line-height: 1.22;
    color: #ffffff;
    text-transform: uppercase;
  }
  .mission .hl { color: var(--lime-text); }
  .brand-panel {
    position: absolute;
    right: 0; top: 0; bottom: 0;
    width: 210px;
    background: var(--lime);
  }
  .edge-stripe {
    position: absolute;
    top: 0; bottom: 0;
    left: 458px;
    width: 12px;
    display: flex;
    flex-direction: column;
  }
  .edge-stripe .seg-navy { flex: 1.4; background: var(--navy-blue); }
  .edge-stripe .seg-sky  { flex: 1;   background: var(--sky-blue); }
  .edge-stripe .seg-forest { flex: 1.2; background: var(--forest); }
  .brand-panel .brand-name {
    position: absolute;
    left: 50%; top: 50%;
    transform: translate(-50%, -50%) rotate(-90deg);
    white-space: nowrap;
    display: flex;
    align-items: center;
    gap: 12px;
    font-family: "Montserrat", sans-serif;
    font-weight: 400;
    font-size: 34px;
    color: #ffffff;
  }
  .brand-square {
    width: 20px; height: 20px;
    background: #ffffff;
    display: inline-block;
  }

  /* Front side */
  .card-front { top: 469px; background: var(--card-white); }
  .front-brand {
    position: absolute;
    right: 42px; top: 46px;
    display: flex;
    align-items: center;
    gap: 12px;
    font-family: "Montserrat", sans-serif;
    font-weight: 400;
    font-size: 40px;
    color: var(--lime);
  }
  .front-brand .brand-square { background: var(--lime); width: 22px; height: 22px; }
  .person { position: absolute; left: 42px; top: 150px; right: 42px; }
  .person-name {
    font-weight: 700;
    font-size: 42px;
    color: var(--ink);
    letter-spacing: 0.5px;
    line-height: 1;
  }
  .person-title {
    font-size: 19px;
    color: var(--label-blue);
    margin-top: 6px;
    padding-bottom: 8px;
    border-bottom: 2px solid var(--rule-green);
    width: 330px;
  }
  .phones {
    display: flex;
    gap: 36px;
    font-size: 30px;
    color: var(--ink);
    margin-top: 12px;
    padding-bottom: 10px;
    border-bottom: 2px solid var(--rule-green);
  }
  .phones .label { color: var(--label-blue); font-size: 24px; margin-right: 6px; }
  .web-line {
    margin-top: 12px;
    font-size: 19px;
    color: var(--muted);
  }
</style>
</head>
<body>

  <section class="card card-back" aria-label="Card back">
    <p class="mission">
      I equip results <span class="hl">oriented</span>
      <span class="hl">business leaders</span> to turn
      their <span class="hl">people problems</span> into
      profits in <span class="hl">six months</span>
      or <span class="hl">less.</span>
    </p>
    <div class="edge-stripe">
      <span class="seg-navy"></span>
      <span class="seg-sky"></span>
      <span class="seg-forest"></span>
    </div>
    <div class="brand-panel">
      <div class="brand-name"><span class="brand-square"></span>Brightmoor Lane Inc</div>
    </div>
  </section>

  <section class="card card-front" aria-label="Card front">
    <div class="front-brand"><span class="brand-square"></span>Brightmoor Lane Inc</div>
    <div class="person">
      <h1 class="person-name">DANA MERRICK</h1>
      <p class="person-title">CHIEF PERFORMANCE STRATEGIST</p>
      <p class="phones">
        <span><span class="label">PHONE:</span>248-555-0142</span>
        <span><span class="label">MOBILE:</span>248-555-0187</span>
      </p>
      <p class="web-line">danam@brightmoorlane.com &nbsp;|&nbsp; www.brightmoorlane.com</p>
    </div>
  </section>

</body>
</html>
```